Create Vertical Dog Food Labels (3 inches x 5 inches) for PupKitchen

We need a packing Vertical label (3 inches x 5 inches) design for our line of Dog Food - Pup Kitchen at pupkitchenmeals.com (please review website). This design is for Custom Roll Labels. We have a logo already. Use our logo colors on label. What we need incorporated is a list of our ingredients:

50% Choice Beef
20% Pasture-raised Chicken
15% Brown Rice
15% Fresh Vegetables - Carrots, Kale, Zucchini
Meadow Wellness Mix

We also need these lines at the bottom of the label:

Keeps in fridge for 4 days after thawing
Stores in freezer up to 6 months
Questions? email us at orders@meadowlanepantry.com

We have attached a sample of a competitor. The Kibble Crate.

Target Market(s)

Dog owners

Industry/Entity Type

Dog Food

Font styles to use
Sans Serif

Requirements
Must have
• Read project description above
Nice to have
• Our logo color incorporated
Should not have
• I want it simple.

```html
<!DOCTYPE html>
<html lang="en">
<head>
<meta charset="utf-8">
<title>PupKitchen – Vertical Dog Food Label</title>
<link rel="stylesheet" href="https://fonts.googleapis.com/css2?family=Gochi+Hand&family=Amatic+SC:wght@700&display=swap">
<style>
  :root {
    --backdrop: #eceeed;
    --kraft: #c4a48b;
    --card: #ffffff;
    --ink: #2a2a2a;
    --green: #3b7a2e;
    --orange: #e0562a;
    --art-tone: #f2f0ec;
  }
  * { box-sizing: border-box; margin: 0; padding: 0; }
  html, body { width: 1200px; height: 1200px; overflow: hidden; background: #fff; }
  .canvas { position: relative; width: 1200px; height: 1200px; background: #fff; }
  .label-backdrop { position: absolute; left: 267px; top: 64px; width: 666px; height: 1072px; background: var(--backdrop); }
  .label { position: absolute; left: 296px; top: 109px; width: 608px; height: 981px; background: var(--kraft); }
  .panel {
    position: absolute; left: 62px; top: 88px; width: 484px; height: 805px;
    background: var(--card); border-radius: 26px;
    font-family: "Gochi Hand", sans-serif; color: var(--ink); text-align: center;
  }
  .brand { position: absolute; left: 114px; top: 44px; height: 80px; display: flex; align-items: center; gap: 16px; }
  .brand-dot { width: 80px; height: 80px; border-radius: 50%; background: var(--green); }
  .brand-name { font-size: 30px; color: var(--green); line-height: 1; padding-top: 10px; }
  .dog-art { position: absolute; left: 42px; top: 162px; width: 400px; height: 145px; background: var(--art-tone); border-radius: 8px; }
  .intro { position: absolute; left: 20px; top: 350px; width: 444px; font-size: 15px; line-height: 24px; white-space: nowrap; }
  .rule { position: absolute; left: 46px; width: 389px; height: 0; border-top: 1.5px solid var(--ink); }
  .rule.top { top: 489px; }
  .rule.mid { top: 620px; }
  .rule.end { top: 766px; }
  .ingredients { position: absolute; left: 0; top: 514px; width: 484px; height: 84px; }
  .ingredient {
    position: absolute; top: 0; height: 84px; display: flex; flex-direction: column; justify-content: center;
    font-family: "Amatic SC", sans-serif; font-weight: 700; font-size: 19px; line-height: 20px;
    text-transform: uppercase; white-space: nowrap;
    transform: translateX(-50%);
  }
  .ingredient.orange { color: var(--orange); }
  .ingredient.green { color: var(--green); }
  .veg-icons { display: block; margin: 3px auto 0; width: 44px; height: 14px; background: #d9e8d2; border-radius: 4px; }
  .divider { position: absolute; top: 0; height: 84px; border-left: 1.5px solid var(--ink); }
  .storage { position: absolute; left: 0; width: 484px; font-size: 18px; line-height: 1; white-space: nowrap; }
  .storage.orange { color: var(--orange); }
  .storage.green { color: var(--green); }
</style>
</head>
<body>
<div class="canvas">
  <div class="label-backdrop"></div>
  <div class="label">
    <div class="panel">
      <div class="brand">
        <span class="brand-dot"></span>
        <span class="brand-name">PupKitchen</span>
      </div>

      <div class="dog-art" role="img" aria-label="Line-drawn illustration of three happy cartoon dogs"></div>

      <p class="intro">our exclusive 'Meadow Wellness Mix' blends are all-natural,<br>targeted add-ons that address specific canine health concerns.<br>From turmeric for inflammation to chamomile for calming,<br>each blend transforms meals into health-enhancing<br>solutions tailored to your dog's unique needs.</p>

      <div class="rule top"></div>

      <div class="ingredients">
        <div class="ingredient orange" style="left:61px">50%<br>Choice<br>Beef</div>
        <div class="divider" style="left:96px"></div>
        <div class="ingredient green" style="left:154px">20%<br>Pasture-raised<br>Chicken</div>
        <div class="divider" style="left:212px"></div>
        <div class="ingredient orange" style="left:246px">15%<br>Brown<br>Rice</div>
        <div class="divider" style="left:280px"></div>
        <div class="ingredient green" style="left:328px">15%<br>Fresh<br>Vegetables<span class="veg-icons" role="img" aria-label="Small drawings of zucchini, carrot and kale"></span></div>
        <div class="divider" style="left:376px"></div>
        <div class="ingredient orange" style="left:415px">Meadow<br>Wellness<br>Mix</div>
      </div>

      <div class="rule mid"></div>

      <p class="storage orange" style="top:643px">Keeps in fridge for 4 days after thawing</p>
      <p class="storage green" style="top:684px">Stores in freezer up to 6 months</p>
      <p class="storage orange" style="top:724px">Questions? email us at orders@meadowlanepantry.com</p>

      <div class="rule end"></div>
    </div>
  </div>
</div>
</body>
</html>
```